Brookfield Homes Business Card Design Project

Please create a custom Business Card Design for Brookfield Homes. The logo is attached to this brief.Please include space for
Name Surname
Title (Solutions Specialist)
Phone
Email
Website
Industry/Entity Type
Business
Contact Information for Business Card
Reverse should be printed horizontally and have the following components:
Small version of the logo. (lowest priority)
The words "Real Estate Solutions Company"
A bulleted list (Note: Line breaks are suggestions only):
* BUY, RENOVATE, SELL and RENT:
RESIDENTIAL PROPERTIES
* MAKE CASH OFFERS ON HOUSES IN
ANY CONDITION and IN ANY SITUATION
* SELL PROPERTIES TO INVESTORS
* SOLVE COMPLEX REAL ESTATE
PROBLEMS and TITLE ISSUES
* PRIVATE MONEY INVESTMENT SERVICES
* PAY CASH REWARDS FOR REFERRALS
Included somewhere on the reverse should also be the following:
Office: (318) 642-5591
www.BrookfieldHomes.example
space for fair trade merchants council logo
Look and feel
Each slider illustrates characteristics of the customer's brand and the style your logo design should communicate.

```html
<!DOCTYPE html>
<html lang="en">
<head>
<meta charset="utf-8">
<title>Brookfield Homes — Business Card</title>
<link rel="stylesheet" href="https://fonts.googleapis.com/css2?family=Arimo:wght@400;700&display=swap">
<style>
  :root {
    --backdrop: #eceef0;
    --card: #ffffff;
    --sunshine: #edc958;
    --brand-blue: #2f6db3;
    --leaf: #8cbf4a;
    --on-sun: #ffffff;
    --ink-soft: #4a5866;
    --shadow: rgba(40, 50, 60, 0.14);
  }
  * { box-sizing: border-box; margin: 0; padding: 0; }
  html, body {
    width: 1200px;
    height: 720px;
    overflow: hidden;
    background: var(--backdrop);
    font-family: "Arimo", Arial, sans-serif;
  }
  .canvas { position: relative; width: 1200px; height: 720px; }
  .card {
    position: absolute;
    width: 520px;
    height: 300px;
    background: var(--card);
    box-shadow: 0 10px 28px var(--shadow);
    overflow: hidden;
  }
  .brand { display: flex; align-items: center; gap: 8px; }
  .brand-dot {
    width: 16px; height: 16px; border-radius: 50%;
    background: var(--sunshine); flex: none;
  }
  .brand-name {
    color: var(--brand-blue);
    font-weight: 700;
    letter-spacing: 0.05em;
    text-transform: uppercase;
    line-height: 1.1;
  }

  /* Contact side */
  .card--contact { left: 50px; top: 80px; }
  .contact__brand {
    position: absolute; left: 28px; top: 50%;
    transform: translateY(-50%);
  }
  .contact__brand .brand-name { font-size: 14px; }
  .contact__panel {
    position: absolute; right: 0; bottom: 0;
    width: 320px; height: 300px;
  }
  .contact__panel path { fill: var(--sunshine); }
  .contact__details {
    position: absolute; right: 20px; bottom: 22px;
    text-align: right; color: var(--on-sun);
    font-style: normal; font-size: 13px; line-height: 1.45;
  }
  .contact__name { font-size: 18px; font-weight: 700; }
  .contact__title { font-size: 12px; margin-bottom: 4px; }
  .contact__web { margin-top: 2px; }

  /* Reverse side */
  .card--reverse {
    left: 630px; top: 340px;
    padding: 20px 24px 18px;
    display: flex; flex-direction: column; align-items: center;
  }
  .reverse__brand .brand-name { font-size: 15px; }
  .reverse__tagline {
    margin-top: 8px;
    color: var(--sunshine);
    font-size: 13px; font-weight: 700;
    letter-spacing: 0.06em; text-transform: uppercase;
  }
  .services {
    list-style: none;
    margin-top: 12px;
    align-self: stretch;
    color: var(--ink-soft);
    font-size: 10px; line-height: 1.6;
    text-transform: uppercase; letter-spacing: 0.02em;
  }
  .services li { position: relative; padding-left: 14px; }
  .services li::before {
    content: ""; position: absolute; left: 2px; top: 5px;
    width: 6px; height: 6px; border-radius: 50%;
    background: var(--leaf);
  }
  .reverse__footer {
    margin-top: auto; align-self: stretch;
    display: flex; align-items: center; justify-content: space-between;
    border-top: 1px solid var(--sunshine);
    padding-top: 10px;
    color: var(--brand-blue); font-size: 11px; font-weight: 700;
  }
  .badge-slot {
    width: 30px; height: 30px;
    background: var(--backdrop); border-radius: 4px;
  }
</style>
</head>
<body>
  <main class="canvas">
    <section class="card card--contact" aria-label="Business card, contact side">
      <div class="brand contact__brand">
        <span class="brand-dot"></span>
        <span class="brand-name">Brookfield Homes</span>
      </div>
      <svg class="contact__panel" viewBox="0 0 320 300" aria-hidden="true">
        <path d="M0 300 V245 C0 205 40 185 80 192 C78 112 150 38 240 38 H320 V300 Z"/>
      </svg>
      <address class="contact__details">
        <p class="contact__name">Mara Ellison</p>
        <p class="contact__title">Solutions Specialist</p>
        <p class="contact__phone">02 5550 1942</p>
        <p class="contact__phone">04 5550 7316</p>
        <p class="contact__email">mara.ellison@brookfieldhomes.example</p>
        <p class="contact__web">www.brookfieldhomes.example</p>
      </address>
    </section>

    <section class="card card--reverse" aria-label="Business card, reverse side">
      <div class="brand reverse__brand">
        <span class="brand-dot"></span>
        <span class="brand-name">Brookfield Homes</span>
      </div>
      <p class="reverse__tagline">Real Estate Solutions Company</p>
      <ul class="services">
        <li>Buy, renovate, sell and rent: residential properties</li>
        <li>Make cash offers on houses in any condition and in any situation</li>
        <li>Sell properties to investors</li>
        <li>Solve complex real estate problems and title issues</li>
        <li>Private money investment services</li>
        <li>Pay cash rewards for referrals</li>
      </ul>
      <div class="reverse__footer">
        <span class="reverse__office">Office: (318) 642-5591</span>
        <span class="reverse__web">www.BrookfieldHomes.example</span>
        <span class="badge-slot" role="img" aria-label="Space for fair trade merchants council badge"></span>
      </div>
    </section>
  </main>
</body>
</html>
```